body therapist

I need to offer my services as a massage therapist at home, acclimating customer space aroma candles with music and everything else to bring comfort. 8 offer rituals like this: relaxing ritual, purifying ritual, ritual breast, facial and body cleansing ritual organic, ritual man, ritual feet, slimming ritual. Naraja handling colors, seawater, green, lavender

Target Market(s)

men and women, tired, stressed, looking for something new

Font styles to use
Decorative
Script

Colors
f37122
0493ce
abd037

Requirements
Must have
• detailing each massage
Nice to have
• simple and elegant

```html
<!DOCTYPE html>
<html lang="es">
<head>
<meta charset="utf-8">
<title>Terapia Serena – Folleto</title>
<link href="https://fonts.googleapis.com/css2?family=Italianno&family=Sorts+Mill+Goudy&family=Cormorant+Garamond:ital,wght@1,600;1,700&display=swap" rel="stylesheet">
<style>
  :root{
    --page-bg:#f2f2f2;
    --panel-edge:#ebe9ea;
    --panel-white:#fbfbfb;
    --taupe:#cdbfb8;
    --taupe-line:#b3a199;
    --ink:#2e1e1a;
    --ink-soft:#3b2b27;
    --skin:#e2b391;
    --skin-light:#f1d7c2;
    --linen:#f4f1ef;
    --naranja:#f37122;
    --marino:#0493ce;
    --verde:#abd037;
    --lavanda:#9b87c4;
  }
  *{box-sizing:border-box;margin:0;padding:0}
  html,body{width:1200px;height:1200px;overflow:hidden;background:var(--page-bg)}
  .spread{position:absolute;left:40px;top:110px;width:1120px;height:980px;display:flex;box-shadow:0 10px 30px rgba(0,0,0,.12)}
  .panel{position:relative;width:560px;height:980px;overflow:hidden}
  .panel--inside{background:var(--panel-edge)}
  .panel--cover{background:var(--panel-white);border-left:1px solid #e2e0e0}

  .info-box{position:absolute;left:74px;width:410px;background:var(--taupe)}
  .info-box--top{top:0;height:262px;padding:44px 30px 0 32px}
  .info-box--bottom{top:718px;height:262px;padding:26px 40px 0 38px}
  .script-title{font-family:"Italianno",cursive;color:var(--ink);font-size:40px;line-height:1;font-weight:400;white-space:nowrap}
  .rate-note{font-family:"Sorts Mill Goudy",serif;color:var(--ink);font-size:17px;line-height:1.5;margin-top:26px;text-align:justify}

  .rule{position:absolute;left:0;width:560px;height:6px;background:var(--taupe-line)}
  .photo{position:absolute}
  .photo--inside{left:0;top:268px;width:560px;height:444px;
    background:linear-gradient(100deg,var(--linen) 0%,var(--skin-light) 22%,var(--skin) 48%,var(--skin-light) 70%,var(--linen) 100%)}
  .photo--cover{left:0;top:655px;width:560px;height:250px;
    background:linear-gradient(110deg,var(--linen) 0%,var(--skin-light) 25%,var(--skin) 55%,var(--skin-light) 78%,#fafafa 100%)}

  .contact{position:absolute;font-family:"Cormorant Garamond",serif;font-style:italic;font-weight:700;color:var(--ink)}
  .contact--inside{left:100px;top:565px;text-align:center;width:270px}
  .phone{display:flex;align-items:center;justify-content:center;gap:8px;font-size:32px}
  .phone svg{width:20px;height:22px;fill:var(--ink)}
  .hours{font-size:21px;line-height:1.35;margin-top:12px}

  .prices-title{font-family:"Sorts Mill Goudy",serif;font-weight:700;font-size:25px;color:var(--ink)}
  .prices{list-style:none;margin-top:4px}
  .prices li{display:flex;justify-content:space-between;font-family:"Sorts Mill Goudy",serif;font-size:27px;line-height:1.26;color:var(--ink)}
  .tagline{font-family:"Italianno",cursive;font-size:40px;color:var(--ink);text-align:center;margin-top:20px}

  .brand{position:absolute;left:0;width:560px;top:60px;display:flex;align-items:center;justify-content:center;gap:16px}
  .brand-mark{width:16px;height:16px;border-radius:50%;background:var(--ink)}
  .brand-name{font-family:"Italianno",cursive;font-size:74px;color:var(--ink);line-height:1}
  .accent-bar{position:absolute;left:190px;top:150px;width:180px;height:3px;
    background:linear-gradient(90deg,var(--naranja) 0 25%,var(--marino) 25% 50%,var(--verde) 50% 75%,var(--lavanda) 75% 100%)}
  .cover-intro{position:absolute;left:30px;width:500px;top:172px;text-align:center;font-family:"Italianno",cursive;font-size:29px;line-height:1.35;color:var(--ink-soft)}

  .rituals{position:absolute;left:44px;top:300px;width:472px;list-style:none}
  .rituals-title{font-family:"Italianno",cursive;font-size:36px;color:var(--ink);text-align:center;line-height:1;margin-bottom:8px}
  .ritual{display:flex;gap:10px;align-items:flex-start;margin-bottom:6px}
  .ritual-dot{flex:none;width:10px;height:10px;border-radius:50%;margin-top:7px}
  .ritual-name{font-family:"Cormorant Garamond",serif;font-style:italic;font-weight:700;font-size:18px;line-height:1.1;color:var(--ink)}
  .ritual-detail{font-family:"Sorts Mill Goudy",serif;font-size:13.5px;line-height:1.25;color:var(--ink-soft)}
  .dot--naranja{background:var(--naranja)}
  .dot--marino{background:var(--marino)}
  .dot--verde{background:var(--verde)}
  .dot--lavanda{background:var(--lavanda)}

  .contact--cover{left:0;width:560px;top:925px}
</style>
</head>
<body>
<main class="spread">
  <section class="panel panel--inside">
    <div class="info-box info-box--top">
      <h2 class="script-title">Terapeuta de masajes a domicilio</h2>
      <p class="rate-note">La tarifa de precios se aplica por tiempo de servicio, independientemente del tipo de masaje solicitado</p>
    </div>
    <div class="rule" style="top:262px"></div>
    <div class="photo photo--inside" role="img" aria-label="Fotografía de un hombre recostado recibiendo un masaje en la espalda sobre una camilla blanca"></div>
    <div class="contact contact--inside">
      <div class="phone">
        <svg viewBox="0 0 20 22" aria-hidden="true"><path d="M4 1l3 5-2 2c1 3 4 7 7 8l2-2 5 3-2 4C9 21 0 12 1 3z"/></svg>
        <span>1 800-555-0142</span>
      </div>
      <p class="hours">Lunes a Sabado<br>8 a 21 hrs.</p>
    </div>
    <div class="rule" style="top:712px"></div>
    <div class="info-box info-box--bottom">
      <h3 class="prices-title">Precios:</h3>
      <ul class="prices">
        <li><span>30 Minutos</span><span>20 €</span></li>
        <li><span>60 Minutos</span><span>40 €</span></li>
        <li><span>90 Minutos</span><span>60 €</span></li>
      </ul>
      <p class="tagline">Disfruta de un masaje relajante</p>
    </div>
  </section>

  <section class="panel panel--cover">
    <div class="brand">
      <span class="brand-mark"></span>
      <span class="brand-name">Terapia Serena</span>
    </div>
    <div class="accent-bar"></div>
    <p class="cover-intro">Terapeuta de masajes a domicilio<br>ambientando el espacio del cliente con música, aromas velas<br>y todo lo demas para brindar bienestar y mejor salud.</p>

    <ul class="rituals">
      <li class="rituals-title">Nuestros rituales</li>
      <li class="ritual"><span class="ritual-dot dot--naranja"></span><div><p class="ritual-name">Ritual Relajante</p><p class="ritual-detail">Masaje suave con aceites aromáticos que libera tensión y estrés.</p></div></li>
      <li class="ritual"><span class="ritual-dot dot--marino"></span><div><p class="ritual-name">Ritual Purificante</p><p class="ritual-detail">Drenaje y sales marinas que eliminan toxinas del cuerpo.</p></div></li>
      <li class="ritual"><span class="ritual-dot dot--verde"></span><div><p class="ritual-name">Ritual de Pecho</p><p class="ritual-detail">Masaje delicado que favorece la circulación y la firmeza.</p></div></li>
      <li class="ritual"><span class="ritual-dot dot--lavanda"></span><div><p class="ritual-name">Ritual de Limpieza Orgánica Facial y Corporal</p><p class="ritual-detail">Exfoliación e hidratación con productos naturales.</p></div></li>
      <li class="ritual"><span class="ritual-dot dot--naranja"></span><div><p class="ritual-name">Ritual Hombre</p><p class="ritual-detail">Masaje profundo de espalda y hombros para el cansancio.</p></div></li>
      <li class="ritual"><span class="ritual-dot dot--marino"></span><div><p class="ritual-name">Ritual de Pies</p><p class="ritual-detail">Reflexología y baño tibio que renuevan la energía.</p></div></li>
      <li class="ritual"><span class="ritual-dot dot--verde"></span><div><p class="ritual-name">Ritual Reductor</p><p class="ritual-detail">Masaje modelador que ayuda a tonificar y afinar la silueta.</p></div></li>
    </ul>

    <div class="photo photo--cover" role="img" aria-label="Fotografía de una mujer con una flor blanca en el cabello recibiendo un masaje en los hombros"></div>
    <div class="contact contact--cover">
      <div class="phone">
        <svg viewBox="0 0 20 22" aria-hidden="true"><path d="M4 1l3 5-2 2c1 3 4 7 7 8l2-2 5 3-2 4C9 21 0 12 1 3z"/></svg>
        <span>1 800-555-0142</span>
      </div>
    </div>
  </section>
</main>
</body>
</html>
```